New emergency medical service needs a marketing flyer for prospective customers

We need a tri fold brochure on an 8.5 X 11 stock for a new emergency medical service in Pennsylvania. We provide basic first aid and now Covid-19 pre screening and temperature monitoring for special events, large gatherings and businesses. Examples of these would be but not limited to: Sporting events, carnivals, festivals, craft shows, warehouses, churches, manufacturing facilities, industrial buildings, large construction sites, multi occupancy officer buildings. The market for this is pretty much untouched and endless. we would like to use gray as the back ground color and obviously our logo. The final design should grab their attention and communicate the importance of having trained and certified professionals at their event or facility. We want to give them that piece of mind they are in good hands with us.

Target Market(s)

primary focus is going to be on businesses with large offices, large buildings or lots of foot traffic in and out of the building

Requirements
Must have
• gray background, pictures, company phone # , company web site, and contact email address. I will provide all that information to the winner to add at the end.
Nice to have
• pictures that covers the whole front cover with logo at top

```html
<!DOCTYPE html>
<html lang="en">
<head>
<meta charset="utf-8">
<title>Ardent Medics – Tri-fold Brochure</title>
<link rel="stylesheet" href="https://fonts.googleapis.com/css2?family=Montserrat:wght@600;700;800&family=Open+Sans:wght@400;600&display=swap">
<style>
:root{
  --canvas:#f4f5f6;
  --paper:#ffffff;
  --panel-gray:#eef0f2;
  --blue:#1b3fa6;
  --blue-deep:#142f86;
  --teal:#1aa7a8;
  --ink:#2b2f36;
  --muted:#6b7280;
  --photo-a:#cfdde6;
  --photo-b:#8fb3c6;
  --placeholder:#d9dcdf;
}
*{box-sizing:border-box;margin:0;padding:0}
html,body{width:800px;height:1200px;overflow:hidden;background:var(--canvas)}
body{font-family:"Open Sans",sans-serif;color:var(--ink);position:relative}
.spread{position:absolute;left:30px;width:740px;height:572px;background:var(--paper);display:grid;grid-template-columns:repeat(3,1fr);box-shadow:0 4px 14px rgba(0,0,0,.12)}
.spread--outside{top:18px}
.spread--inside{top:608px}
.panel{position:relative;overflow:hidden;border-right:1px solid #e3e6e9}
.panel:last-child{border-right:none}
.pad{padding:22px 20px}
h2{font-family:"Montserrat",sans-serif;font-weight:800;font-size:12px;letter-spacing:.5px;color:var(--blue);margin-bottom:8px;text-transform:uppercase}
p{font-size:8.5px;line-height:1.6;color:var(--muted);margin-bottom:8px}
.brand{display:flex;align-items:center;gap:6px;font-family:"Montserrat",sans-serif;font-weight:800;color:var(--blue);font-size:15px}
.brand .dot{width:14px;height:14px;border-radius:50%;background:var(--blue)}
.photo{background:linear-gradient(135deg,var(--photo-a),var(--photo-b))}
.placeholder-box{background:var(--placeholder);height:150px;margin-top:12px}
/* outside middle */
.contact-photo{height:190px;margin-top:14px}
.contact{background:var(--blue);color:#fff;padding:16px 20px;height:100%}
.contact h2{color:#fff}
.contact-row{display:flex;align-items:center;gap:8px;font-size:9px;margin-bottom:8px}
.contact-row svg{flex:none}
/* cover */
.cover{background:var(--panel-gray)}
.cover .brand{position:absolute;top:18px;right:18px;z-index:2}
.cover-photo{position:absolute;inset:0 0 170px 0}
.cover-band{position:absolute;left:0;right:0;bottom:0;height:170px;background:linear-gradient(120deg,var(--teal),var(--blue));padding:24px 20px;color:#fff}
.cover-title{font-family:"Montserrat",sans-serif;font-weight:800;font-size:30px;line-height:1;margin-bottom:10px}
.cover-sub{font-family:"Montserrat",sans-serif;font-weight:700;font-size:12px;line-height:1.35;text-transform:uppercase}
/* inside */
.inside-photo{height:140px;margin:6px 0 14px}
.why{background:linear-gradient(180deg,var(--teal),var(--blue));color:#fff;height:100%}
.why h2{color:#fff}
.why p{color:#e6f1f8}
.service-list{list-style:none;margin-top:6px}
.service-list li{display:flex;align-items:center;gap:8px;font-size:9px;font-weight:600;margin-bottom:10px}
.tick{width:14px;height:14px;border-radius:50%;background:#fff;display:flex;align-items:center;justify-content:center;flex:none}
.benefit-photo{height:190px}
.benefits{padding:16px 18px}
.benefit{display:flex;gap:8px;margin-bottom:10px;align-items:center}
.benefit-thumb{width:40px;height:32px;flex:none}
.benefit-bar{flex:1;background:var(--teal);color:#fff;font-size:8px;line-height:1.35;padding:5px 8px}
.benefit:nth-child(even) .benefit-bar{background:var(--blue)}
</style>
</head>
<body>

<section class="spread spread--outside">
  <div class="panel pad">
    <h2>About Us</h2>
    <p>We bring trained, certified medical staff to your event or site. Our team offers first aid, health screening and calm support so every guest and worker stays safe from start to finish.</p>
    <p>Call us to plan coverage for your next gathering.</p>
    <div class="placeholder-box"></div>
    <p style="margin-top:12px">Serving offices, warehouses, venues and building sites across the state with fast, friendly care.</p>
  </div>
  <div class="panel" style="display:flex;flex-direction:column">
    <div class="pad" style="padding-bottom:0"><div class="brand"><span class="dot"></span>Ardent Medics</div></div>
    <div class="photo contact-photo" role="img" aria-label="Lab technician in protective suit working with samples"></div>
    <div class="contact">
      <h2>Contact Us</h2>
      <div class="contact-row"><svg width="12" height="12" viewBox="0 0 24 24"><path fill="#fff" d="M6.6 10.8a15 15 0 006.6 6.6l2.2-2.2a1 1 0 011-.25 11.4 11.4 0 003.6.57 1 1 0 011 1V20a1 1 0 01-1 1A17 17 0 013 4a1 1 0 011-1h3.5a1 1 0 011 1c0 1.25.2 2.45.57 3.57a1 1 0 01-.25 1z"/></svg>555-014-2880</div>
      <div class="contact-row"><svg width="12" height="12" viewBox="0 0 24 24"><rect x="2" y="5" width="20" height="14" rx="2" fill="none" stroke="#fff" stroke-width="2"/><path d="M3 6l9 7 9-7" fill="none" stroke="#fff" stroke-width="2"/></svg>care@ardentmedics.com</div>
      <div class="contact-row"><svg width="12" height="12" viewBox="0 0 24 24"><circle cx="12" cy="12" r="9" fill="none" stroke="#fff" stroke-width="2"/><path d="M3 12h18M12 3c3 3 3 15 0 18M12 3c-3 3-3 15 0 18" fill="none" stroke="#fff" stroke-width="1.5"/></svg>www.ardentmedics.com</div>
    </div>
  </div>
  <div class="panel cover">
    <div class="brand"><span class="dot"></span>Ardent Medics</div>
    <div class="photo cover-photo" role="img" aria-label="Doctor in white coat and face mask with stethoscope"></div>
    <div class="cover-band">
      <div class="cover-title">COVID-19</div>
      <div class="cover-sub">Pre screening and temperature monitoring for special events</div>
    </div>
  </div>
</section>

<section class="spread spread--inside">
  <div class="panel pad">
    <h2>About Us</h2>
    <p>Our certified team gives peace of mind at busy sites. We screen, monitor and treat on the spot, so your people feel safe and your event keeps moving.</p>
    <div class="photo inside-photo" role="img" aria-label="Scientist in protective gear inside a laboratory"></div>
    <h2>Medical Care Kit</h2>
    <p>Each crew arrives with a full first aid kit, thermometers, masks and clean supplies ready for any need on site.</p>
  </div>
  <div class="panel why pad">
    <h2>Why Choose Us</h2>
    <p>Trained professionals, quick response and clear reports. We fit your schedule and keep every guest in good hands all day long.</p>
    <h2 style="margin-top:14px">Our Medical Services</h2>
    <ul class="service-list">
      <li><span class="tick"><svg width="8" height="8" viewBox="0 0 10 10"><path d="M1.5 5l2.5 2.5 4.5-5" fill="none" stroke="#1b3fa6" stroke-width="2"/></svg></span>Basic First Aid</li>
      <li><span class="tick"><svg width="8" height="8" viewBox="0 0 10 10"><path d="M1.5 5l2.5 2.5 4.5-5" fill="none" stroke="#1b3fa6" stroke-width="2"/></svg></span>Health Pre Screening</li>
      <li><span class="tick"><svg width="8" height="8" viewBox="0 0 10 10"><path d="M1.5 5l2.5 2.5 4.5-5" fill="none" stroke="#1b3fa6" stroke-width="2"/></svg></span>Temperature Checks</li>
      <li><span class="tick"><svg width="8" height="8" viewBox="0 0 10 10"><path d="M1.5 5l2.5 2.5 4.5-5" fill="none" stroke="#1b3fa6" stroke-width="2"/></svg></span>Event Standby Crew</li>
      <li><span class="tick"><svg width="8" height="8" viewBox="0 0 10 10"><path d="M1.5 5l2.5 2.5 4.5-5" fill="none" stroke="#1b3fa6" stroke-width="2"/></svg></span>Site Safety Reports</li>
    </ul>
  </div>
  <div class="panel" style="background:var(--panel-gray)">
    <div class="photo benefit-photo" role="img" aria-label="Health worker taking a test sample from a patient"></div>
    <div class="benefits">
      <h2>Our Benefits Solutions</h2>
      <div class="benefit"><div class="photo benefit-thumb" role="img" aria-label="Small photo of medical staff"></div><div class="benefit-bar">Certified staff trained for crowds and large sites.</div></div>
      <div class="benefit"><div class="photo benefit-thumb" role="img" aria-label="Small photo of screening station"></div><div class="benefit-bar">Fast screening lines that keep entry moving.</div></div>
      <div class="benefit"><div class="photo benefit-thumb" role="img" aria-label="Small photo of first aid kit"></div><div class="benefit-bar">Full kits and clean gear on every shift.</div></div>
      <div class="benefit"><div class="photo benefit-thumb" role="img" aria-label="Small photo of event crowd"></div><div class="benefit-bar">Flexible plans for events of any size.</div></div>
    </div>
  </div>
</section>

</body>
</html>
```